Quillbrook painting

Am looking for a lawn sign design for my paintings company.
I also attached my business card a example

Phone number of the business +1(204)555-0179
Key words:Free estimates|pressure washing |Residential| Commercial | Interior | Exterior

```html
<!DOCTYPE html>
<html lang="en">
<head>
<meta charset="utf-8">
<title>Quillbrook Painting – Lawn Sign</title>
<link rel="stylesheet" href="https://fonts.googleapis.com/css2?family=Michroma&family=Montserrat:wght@600;800;900&display=swap">
<style>
  :root {
    --backdrop: #9b9d9d;
    --sign-black: #000000;
    --brand-blue: #14a6e0;
    --text-white: #ffffff;
    --divider-blue: #14a6e0;
    --cta-red: #e52629;
    --cta-green: #7cc242;
    --cta-text: #1a1a1a;
    --paint-red: #d1214b;
    --paint-orange: #e8532e;
    --paint-yellow: #e4c85a;
    --paint-teal: #00b0bd;
    --paint-blue: #2f7fc6;
    --paint-purple: #6f3f99;
    --splash-pink: #ec3d8e;
    --splash-magenta: #a81f8d;
    --splash-blue: #3f8fd0;
    --splash-orange: #f26f21;
    --splash-yellow: #fcd829;
  }
  * { margin: 0; padding: 0; box-sizing: border-box; }
  html, body {
    width: 781px; height: 1200px; overflow: hidden;
    background: var(--backdrop);
  }
  .canvas {
    position: relative; width: 781px; height: 1200px;
  }
  .lawn-sign {
    position: absolute; left: 0; top: 307px;
    width: 781px; height: 586px;
    background: var(--sign-black);
    overflow: hidden;
  }
  .paint-drips {
    position: absolute; left: 234px; top: 0;
    width: 547px; height: 215px;
    background: linear-gradient(90deg,
      var(--paint-red) 0%, var(--paint-orange) 18%, var(--paint-yellow) 38%,
      var(--paint-teal) 58%, var(--paint-blue) 78%, var(--paint-purple) 100%);
    -webkit-mask-image: linear-gradient(180deg, #000 55%, transparent 100%);
            mask-image: linear-gradient(180deg, #000 55%, transparent 100%);
  }
  .brand-name {
    position: absolute; left: 0; top: 220px; width: 781px;
    text-align: center;
    font-family: "Michroma", sans-serif;
    color: var(--brand-blue);
    font-size: 48px; line-height: 84px; letter-spacing: -1px;
    text-transform: uppercase;
  }
  .brand-name span { display: block; }
  .service-list {
    position: absolute; left: 0; top: 382px; width: 781px;
    text-align: center;
    font-family: "Montserrat", sans-serif; font-weight: 600;
    font-size: 18px; color: var(--text-white); white-space: nowrap;
  }
  .service-list .divider { color: var(--divider-blue); padding: 0 3px; }
  .estimate-bar {
    position: absolute; left: 54px; top: 431px;
    width: 676px; height: 49px;
    display: flex;
  }
  .estimate-label {
    flex: 0 0 360px;
    background: var(--cta-red);
    font-family: "Montserrat", sans-serif; font-weight: 900;
    font-size: 24px; color: var(--cta-text);
    display: flex; align-items: center; padding-left: 15px;
    white-space: nowrap;
  }
  .phone-pill {
    flex: 1;
    margin-left: -12px;
    background: var(--cta-green);
    border-radius: 25px 0 0 25px;
    display: flex; align-items: center; gap: 6px; padding-left: 14px;
    font-family: "Michroma", sans-serif; font-size: 20px; color: var(--cta-text);
    white-space: nowrap;
  }
  .phone-icon { width: 22px; height: 22px; flex: none; }
  .paint-splashes {
    position: absolute; left: 0; bottom: 0;
    width: 781px; height: 88px;
    background: linear-gradient(90deg,
      var(--splash-pink) 0%, var(--splash-magenta) 25%, var(--splash-blue) 45%,
      var(--splash-orange) 65%, var(--splash-yellow) 85%, var(--sign-black) 100%);
    -webkit-mask-image: linear-gradient(0deg, #000 45%, transparent 100%);
            mask-image: linear-gradient(0deg, #000 45%, transparent 100%);
  }
</style>
</head>
<body>
<main class="canvas">
  <section class="lawn-sign">
    <div class="paint-drips" role="img" aria-label="Rainbow paint dripping down from the top edge"></div>

    <h1 class="brand-name"><span>Quillbrook</span><span>Painting</span></h1>

    <p class="service-list">Pressure Washing<span class="divider">|</span>Residential<span class="divider">|</span>Commercial<span class="divider">|</span>Interior<span class="divider">|</span>Exterior</p>

    <div class="estimate-bar">
      <div class="estimate-label">GET FREE ESTIMATES</div>
      <div class="phone-pill">
        <svg class="phone-icon" viewBox="0 0 24 24" aria-hidden="true">
          <path fill="#e52629" d="M6.6 10.8c1.4 2.8 3.8 5.1 6.6 6.6l2.2-2.2c.3-.3.7-.4 1-.2 1.1.4 2.3.6 3.6.6.6 0 1 .4 1 1V20c0 .6-.4 1-1 1C10.6 21 3 13.4 3 4c0-.6.4-1 1-1h3.5c.6 0 1 .4 1 1 0 1.3.2 2.5.6 3.6.1.3 0 .7-.2 1z"/>
        </svg>
        <span class="phone-number">+1(204)555-0179</span>
      </div>
    </div>

    <div class="paint-splashes" role="img" aria-label="Colourful paint splashes along the bottom edge"></div>
  </section>
</main>
</body>
</html>
```